Investment Memorandum Document

IM for Harbourline Lending Fund - is the document that needs work

Make sure it is all done in MS WORD so that i or lawyers can edit some words if required

the IM is NOT final but its 95% of the way there. Maybe a few more pages and wording changes - but that is something i can do i guess or you can easier adjust

Just to typeset and pretty it all up - a few sample finished products have been uploaded for reference.

KPT IM is the one i like - but feel free to show off your skills

put 1.2 to 1.8 all in contrasting row tables

Target Market(s)

Individual and Institutional investors with money

Industry/Entity Type

Investment Banking

Colors

Designer to choose colors to be used in the design.

Requirements
Must have
• clear professional layout and easy on the eye
• https://www.filebarn-example.net/sh/84m7t55xqk2wbnr/QQzdLeMu8RplbqTYAXNW47Ko?dl=0
• use the link above for high res images
Nice to have
• pictures and graphics
Should not have
• cartoons

```html
<!DOCTYPE html>
<html lang="en">
<head>
<meta charset="utf-8">
<title>Harbourline Asset Management – Information Memorandum</title>
<link href="https://fonts.googleapis.com/css2?family=Didact+Gothic&display=swap" rel="stylesheet">
<style>
  :root {
    --backdrop: #d8d9d3;
    --paper: #f0f3f4;
    --paper-shade: #e4e7e9;
    --teal-deep: #0f2f3c;
    --teal-mid: #1f5a6b;
    --teal-bright: #2d8ea3;
    --gold: #b38a55;
    --ink: #2f3337;
    --ink-soft: #4a4f54;
    --white: #ffffff;
  }
  * { margin: 0; padding: 0; box-sizing: border-box; }
  html, body { width: 1200px; height: 881px; overflow: hidden; }
  body {
    background: var(--backdrop);
    font-family: "Didact Gothic", "Century Gothic", sans-serif;
    color: var(--ink);
    position: relative;
  }

  /* ---------- Cover ---------- */
  .cover {
    position: absolute; left: 103px; top: 50px;
    width: 638px; height: 449px;
    background: var(--paper);
  }
  .cover-photo {
    position: absolute; left: 319px; top: 0; width: 319px; height: 449px;
    background:
      radial-gradient(ellipse at 65% 60%, var(--teal-bright) 0%, rgba(45,142,163,0) 55%),
      linear-gradient(160deg, #1b3b47 0%, var(--teal-mid) 45%, var(--teal-deep) 100%);
  }
  .cover-facets { position: absolute; inset: 0; }
  .cover-brand {
    position: absolute; left: 378px; top: 228px;
    display: flex; align-items: center; gap: 9px;
    color: var(--white);
  }
  .brand-mark { width: 12px; height: 12px; background: var(--gold); }
  .brand-name { line-height: 1; }
  .brand-name .word { display: block; font-size: 24px; letter-spacing: 3px; }
  .brand-name .tag { display: block; font-size: 6px; letter-spacing: 4.2px; margin-top: 3px; }
  .cover-title {
    position: absolute; left: 378px; top: 273px;
    color: #e4eef1; font-size: 10.4px; letter-spacing: 0.5px; font-weight: 400;
    line-height: 13px; text-transform: uppercase;
  }

  /* ---------- Spread ---------- */
  .spread {
    position: absolute; left: 466px; top: 358px;
    width: 639px; height: 452px;
    display: flex;
  }
  .page { position: relative; height: 100%; background: var(--paper); }
  .page-left { width: 322px; }
  .page-right { width: 317px; border-left: 1px solid #dde1e3; }

  .page-brand {
    position: absolute; left: 25px; top: 32px;
    display: flex; align-items: center; gap: 7px; color: var(--ink-soft);
  }
  .page-brand .brand-mark { width: 9px; height: 9px; }
  .page-brand .word { font-size: 17px; letter-spacing: 2px; }
  .page-brand .tag { font-size: 4px; letter-spacing: 3px; margin-top: 2px; }

  .edge-photo {
    position: absolute; left: 0; top: 82px; width: 19px; height: 162px;
    background: linear-gradient(180deg, var(--teal-mid), var(--teal-bright) 55%, var(--teal-deep));
  }

  .contents { position: absolute; left: 60px; top: 80px; width: 214px; }
  .section-title {
    font-size: 13px; color: var(--gold); font-variant: small-caps;
    letter-spacing: 0.4px; font-weight: 400;
  }
  .contents .section-title::after {
    content: ""; display: block; width: 36px; height: 2px;
    background: var(--gold); margin-top: 3px;
  }
  .toc { list-style: none; margin-top: 9px; }
  .toc li {
    display: flex; font-size: 7.2px; letter-spacing: 0.4px;
    text-transform: uppercase; height: 13px; align-items: center;
  }
  .toc .num { width: 20px; }
  .toc .label { flex: 1; }
  .toc .page-no { width: 12px; text-align: right; }

  .notice { position: absolute; left: 52px; top: 52px; width: 226px; }
  .notice .section-title { text-align: center; font-size: 13px; margin-bottom: 9px; }
  .notice p {
    font-size: 5.6px; line-height: 7.6px; font-variant: small-caps;
    text-align: justify; color: var(--ink); margin-bottom: 1.5px;
  }
  .notice h3 {
    font-size: 5.8px; color: var(--gold); text-transform: uppercase;
    font-weight: 400; letter-spacing: 0.3px; margin: 7px 0 3px;
  }
</style>
</head>
<body>

<section class="cover" aria-label="Front cover">
  <div class="cover-photo" role="img" aria-label="Blurred teal photograph of a modern glass office interior"></div>
  <svg class="cover-facets" width="638" height="449" viewBox="0 0 638 449" aria-hidden="true">
    <polygon points="319,0 638,0 319,281" fill="#ffffff" fill-opacity="0.13"/>
    <polygon points="129,449 319,281 319,449" fill="#e3e6e8"/>
    <line x1="129" y1="449" x2="319" y2="281" stroke="#ffffff" stroke-width="1.2"/>
  </svg>
  <div class="cover-brand">
    <span class="brand-mark"></span>
    <span class="brand-name"><span class="word">HARBOURLINE</span><span class="tag">ASSET MANAGEMENT</span></span>
  </div>
  <h1 class="cover-title">Harbourline Lending Fund<br>Information Memorandum</h1>
</section>

<section class="spread" aria-label="Contents and notice spread">
  <article class="page page-left">
    <div class="page-brand">
      <span class="brand-mark"></span>
      <span class="brand-name"><span class="word">HARBOURLINE</span><span class="tag">ASSET MANAGEMENT</span></span>
    </div>
    <div class="edge-photo" role="img" aria-label="Teal photograph strip continued from the cover"></div>
    <nav class="contents">
      <h2 class="section-title">Contents</h2>
      <ol class="toc">
        <li><span class="label">Message from the Managing Director</span><span class="page-no">5</span></li>
        <li><span class="num">1.</span><span class="label">The Fund</span><span class="page-no">6</span></li>
        <li><span class="num">2.</span><span class="label">The Loans</span><span class="page-no">12</span></li>
        <li><span class="num">3.</span><span class="label">Risks</span><span class="page-no">17</span></li>
        <li><span class="num">4.</span><span class="label">Fees and Costs</span><span class="page-no">20</span></li>
        <li><span class="num">5.</span><span class="label">Management of the Fund</span><span class="page-no">22</span></li>
        <li><span class="num">6.</span><span class="label">Taxation Information</span><span class="page-no">26</span></li>
        <li><span class="num">7.</span><span class="label">Additional Information</span><span class="page-no">31</span></li>
        <li><span class="num">8.</span><span class="label">Application Process</span><span class="page-no">34</span></li>
        <li><span class="num">9.</span><span class="label">Glossary</span><span class="page-no">36</span></li>
        <li><span class="num">10.</span><span class="label">Corporate Directory</span><span class="page-no">38</span></li>
      </ol>
    </nav>
  </article>

  <article class="page page-right">
    <div class="notice">
      <h2 class="section-title">Notice</h2>
      <p>This Information Memorandum is dated XXX and is issued by Keystone Private Trustees Pty Ltd, the trustee of the Harbourline Lending Fund (Fund).</p>
      <p>The purpose of this IM is to provide information for prospective investors to decide whether they wish to invest in the Fund.</p>
      <p>The Trustee has appointed Harbourline Asset Management Pty Ltd as the investment manager of the Fund under the Investment Management Agreement. The Investment Manager is an authorised representative of the Trustee.</p>
      <p>The Fund's trust deed provides for different Classes of Units. Different Classes of Units may have different rights and obligations. The performance of different Classes of Units may also differ depending on the investments of that Class. Holders of each Class will be treated fairly.</p>
      <h3>No disclosure required</h3>
      <p>This IM is intended to provide potential investors with information only and does not constitute a product disclosure statement under the Corporations Act 2001 (Act). It has not been lodged with any government body.</p>
      <p>The offer made under this IM is only available to persons who qualify as wholesale clients or sophisticated investors under the Act (Qualified Investors). The Trustee will not issue Units in the Fund to a person unless it is satisfied that the person is a Qualified Investor.</p>
      <h3>Restrictions on distribution</h3>
      <p>This IM does not constitute an offer of Units in any jurisdiction in which such an offer is not authorised, or to any person to whom it is unlawful to make such an offer.</p>
      <p>No action has been taken to register or qualify interests in the Fund outside Australia. It is the responsibility of prospective investors to comply with the relevant laws of any other jurisdiction, including obtaining any requisite governmental or other consent and adhering to any other formality prescribed in such jurisdiction.</p>
      <p>By receiving and viewing this IM, the recipient warrants that they are legally entitled to do so and that they are Qualified Investors. Further, the persons receiving and viewing this IM warrant that the laws of their own jurisdiction do not prohibit them from acquiring interests in the Fund.</p>
      <p>In particular, this product has not been and will not be registered under the US Securities Act and may not be offered or sold in the United States. Neither this IM, the Application Form nor any other material relating to the product may be distributed in the United States or to any US Person.</p>
      <p>With respect to Australian jurisdiction, this IM has been prepared on the basis that prospective investors are wholesale clients or sophisticated investors, not retail clients within the meaning of the Act.</p>
      <p>Accordingly, this IM is not a product disclosure statement and does not contain all of the information that would be included in one.</p>
      <p>The Trustee may in the future take actions to offer interests in the Fund in other jurisdictions.</p>
    </div>
  </article>
</section>

</body>
</html>
```